Verpackungsdesign für Pasta aus Buchweizen
Zielgruppe
Unser Unternehmen KORNIVA sucht ein sehr modernes Verpackungsdesign für Pasta aus Buchweizen.
Unsere Produkte sind in unserem Online Shop und unterscheiden sich durch die herkömmliche Pasta, da wir Buchweizen in die Verarbeitung mit aufnehmen und somit die gesundheitsfördernde Eigenschaft des Buchweizens im Vordergrund steht. Unsere Pasta aus Buchweizenmehl mit klassischem Hartweizengrieß ist in dieser Form noch nicht im stationären Handel erhältlich, deshalb wünschen wir uns ein neues, ansprechendes Verpackungsdesign welches von den Massenprodukten aus den Regalen im Handel heraussticht. Das Design sollte also minimalistisch und sehr modern wirken, und sich deutlich von der Konkurrenz abheben.
Die Zielgruppe richtet sich sowohl an Massen die Pasta in allen Variationen lieben, als auch an ernährungsbewusste Veganer/Vegetarier die Alternativen im Bereich der herkömmlichen Pasta Kochkultur suchen.
PS: Mit dem Verkauf unserer Pasta investieren wir außerdem in den Aufbau und der Infrastruktur des Erzeugerlandes. Durch unser Prinzip „Teilen & Wachsen“ fördern wir mit unseren Gewinnen nachhaltige Projekte in den Erzeugerländern und helfen somit wirtschaftlich benachteiligten Regionen auf der Welt. (Fair Trade)
Aufgabenstellung
Wir besitzen bereits ein Logo und Verpackungen für unsere Pasta Sorten. Das Logo und das Grundgerüst der Stanzform / Verpackungsmaße (inkl. Sichtfenster) soll beibehalten werden (Siehe Anhang). Als Pasta Verpackungen benutzen wir Faltschachteln und Banderolen.
Verpackungsmaße:
- Faltschachtel (90 x 40 x 165 mm)
- Banderole (560 x 70mm)
Der Produktname ist je nach Sorte zu präzisieren:
- Fusilli
- Makkaroni
- Bandnudeln
- Tarhana
Produktgewicht:
- 250g
Eigenschaften:
- Buchweizenmehl
- 100% Vegan
- Kochzeit 3 Minuten
- Liebevolle Handarbeit
WICHTIG:
1) Bitte benutzt die hochgeladene, leere Stanzform für Artwork.
2) Die Designfarbe kann anhand des Aufstellers ausgerichtet werden (CMYK: 0, 20, 32, 0 und 60, 57, 56, 62) es ist aber kein muss und ihr seit frei in der Kreativität.
3) Bitte das Sichtfenster mit Rand wie aktuell auf den Produkten übernehmen (siehe www.korniva.de/shop)
Nach dem Wettbewerb planen wir zusätzlich ein 1zu1 Projekt und würden uns freuen einen Gewinner auszuwählen - Wir freuen uns auf eure Ideen :)

```html
<!DOCTYPE html>
<html lang="de">
<head>
<meta charset="utf-8">
<title>KORNIVA Buchweizen Pasta – Faltschachtel</title>
<link href="https://fonts.googleapis.com/css2?family=Bebas+Neue&family=Montserrat:wght@300;500;600&family=Playfair+Display:ital@1&family=Homemade+Apple&display=swap" rel="stylesheet">
<style>
  :root {
    --stage: #d6d6d6;
    --box-dark: #1e1e1e;
    --box-side: #222222;
    --text-light: #ffffff;
    --text-soft: #d9d9d9;
    --band-peach: #fcd8b5;
    --band-ink: #2a2320;
    --window-rim: #f4dcbf;
    --grain-deep: #a8401d;
    --grain-warm: #d5713a;
    --badge-green: #5a9a3c;
  }
  * { margin: 0; padding: 0; box-sizing: border-box; }
  html, body { width: 1200px; height: 1148px; overflow: hidden; }
  body {
    background: var(--stage);
    font-family: "Montserrat", sans-serif;
    position: relative;
  }
  .carton {
    position: absolute;
    left: 245px; top: 124px;
    width: 709px; height: 900px;
    display: flex;
  }
  .panel { position: relative; height: 100%; }
  .panel--side { width: 218px; background: var(--box-side); border-right: 1px solid #151515; }
  .panel--front { width: 491px; background: var(--box-dark); }

  /* Side panel */
  .side-title { position: absolute; left: 34px; top: 196px; color: var(--text-soft); font-weight: 300; line-height: 1; }
  .side-title__small { font-size: 14px; letter-spacing: 0.5px; }
  .side-title__large { font-size: 34px; margin-top: 4px; letter-spacing: 1px; }
  .features { position: absolute; left: 24px; top: 318px; color: var(--text-light); }
  .features__heading { font-weight: 600; font-size: 18px; margin-bottom: 12px; }
  .features__list { list-style: none; font-size: 12.5px; font-weight: 500; line-height: 1.75; }
  .features__list li::before { content: "• "; }
  .band { position: absolute; top: 450px; height: 60px; background: var(--band-peach); }
  .band--side { left: 0; width: 218px; }
  .vegan-badge { position: absolute; left: 66px; top: 580px; }
  .drops { position: absolute; left: 62px; top: 778px; }
  .side-weight { position: absolute; left: 72px; top: 822px; color: var(--text-soft); font-size: 15px; font-weight: 300; }

  /* Front panel */
  .brand { position: absolute; top: 72px; left: 0; width: 100%; display: flex; justify-content: center; align-items: center; gap: 10px; }
  .brand__dot { width: 14px; height: 14px; border-radius: 50%; background: var(--text-light); }
  .brand__name { font-family: "Bebas Neue", sans-serif; font-size: 34px; color: var(--text-light); letter-spacing: 1px; }
  .product-title { position: absolute; left: 58px; top: 206px; font-family: "Bebas Neue", sans-serif; font-weight: 400; color: var(--text-light); font-size: 82px; line-height: 0.86; }
  .product-title__sub { position: absolute; left: 226px; top: 286px; font-family: "Homemade Apple", cursive; color: var(--text-light); font-size: 20px; transform: rotate(-4deg); }
  .band--front { left: 0; width: 240px; display: flex; align-items: center; justify-content: center; }
  .variety { font-family: "Playfair Display", serif; font-style: italic; font-size: 27px; color: var(--band-ink); letter-spacing: 1px; }
  .windows { position: absolute; left: 0; top: 500px; }
  .front-weight { position: absolute; right: 44px; top: 778px; font-family: "Playfair Display", serif; font-style: italic; font-size: 26px; color: var(--text-light); }
</style>
</head>
<body>
  <main class="carton">
    <section class="panel panel--side">
      <div class="side-title">
        <div class="side-title__small">BUCHWEIZEN</div>
        <div class="side-title__large">PASTA</div>
      </div>
      <div class="features">
        <h2 class="features__heading">Eigenschaften:</h2>
        <ul class="features__list">
          <li>Buchweizenmehl</li>
          <li>100% Vegan</li>
          <li>Kochzeit 3 Minuten</li>
          <li>Liebevolle Handarbeit</li>
        </ul>
      </div>
      <div class="band band--side"></div>
      <svg class="vegan-badge" width="84" height="84" viewBox="0 0 84 84" aria-hidden="true">
        <circle cx="42" cy="42" r="40" fill="var(--badge-green)" stroke="#ffffff" stroke-width="3"/>
      </svg>
      <svg class="drops" width="80" height="30" viewBox="0 0 80 30" aria-hidden="true">
        <g fill="none" stroke="#ffffff" stroke-width="2">
          <path d="M12 2 C6 12 4 16 4 20 a8 8 0 0 0 16 0 C20 16 18 12 12 2Z"/>
          <path d="M40 2 C34 12 32 16 32 20 a8 8 0 0 0 16 0 C48 16 46 12 40 2Z"/>
          <path d="M68 2 C62 12 60 16 60 20 a8 8 0 0 0 16 0 C76 16 74 12 68 2Z"/>
        </g>
      </svg>
      <div class="side-weight">250g ℮</div>
    </section>

    <section class="panel panel--front">
      <div class="brand">
        <span class="brand__dot"></span>
        <span class="brand__name">KORNIVA</span>
      </div>
      <h1 class="product-title">BUCHWEIZEN<br>PASTA</h1>
      <span class="product-title__sub">Buckwheat</span>
      <div class="band band--front"><span class="variety">tarhana</span></div>
      <svg class="windows" width="491" height="420" viewBox="0 0 491 420" role="img" aria-label="Sichtfenster mit Blick auf rotbraune Tarhana-Krümel">
        <defs>
          <linearGradient id="grain" x1="0" y1="0" x2="1" y2="1">
            <stop offset="0" stop-color="var(--grain-warm)"/>
            <stop offset="1" stop-color="var(--grain-deep)"/>
          </linearGradient>
          <path id="leaf" d="M0,-100 C66,-50 66,50 0,100 C-66,50 -66,-50 0,-100Z"/>
        </defs>
        <g fill="url(#grain)" stroke="var(--window-rim)" stroke-width="6">
          <use href="#leaf" transform="translate(250 148) rotate(22) scale(1.05)"/>
          <use href="#leaf" transform="translate(145 276) rotate(-40) scale(0.95)"/>
          <use href="#leaf" transform="translate(285 296) rotate(33) scale(1.03)"/>
        </g>
      </svg>
      <div class="front-weight">250g ℮</div>
    </section>
  </main>
</body>
</html>
```